Photographic Tutorial website

We are looking for a fresh design for a photographic tutorial / workshop website. The website will have the included functions:

* Home (needs to have a login section)
* About Us
* Info about each course / workshop.
* Subscribe to courses and pay online.
* Members Area
* Photo gallery
* Contact us

The website will be implemented with our own made cms. We do not need it to be coded. We have a team ready to do this for us. We only need the PSD layout.

We have attached a mockup design that the client and I have come up with and we need the design to be taken to the next level.

Client also likes:
http://www.vellowindstudio.example/

Photographic Interests

Online

Requirements
Must have
• Must Stand out i.e black backgrounds
Should not have
• Alter the logo in anyway.

```html
<!DOCTYPE html>
<html lang="en">
<head>
<meta charset="utf-8">
<title>Your Frame Friend – Photographic Tuition</title>
<link href="https://fonts.googleapis.com/css2?family=Arimo:wght@400;700&family=Caladea:wght@400;700&display=swap" rel="stylesheet">
<style>
:root{
  --black:#000;
  --header:#141414;
  --panel-dark:#0c0c0c;
  --light-band:#dfe9ea;
  --white:#ffffff;
  --green:#2fb34a;
  --green-bright:#36c755;
  --orange:#e2740f;
  --footer-grey:#3a3a3a;
  --text-light:#d9d9d9;
  --text-muted:#9a9a9a;
  --box-border:#c9cfe0;
  --body-text:#444;
  --field:#6c6c6c;
}
*{margin:0;padding:0;box-sizing:border-box}
html,body{width:675px;height:1200px;overflow:hidden;background:var(--black)}
body{position:relative;font-family:"Arimo",Arial,sans-serif;color:var(--white)}
.abs{position:absolute}

/* header */
.top-bar{left:0;top:0;width:675px;height:42px;background:linear-gradient(#2a2a2a,#0e0e0e)}
.brand{left:44px;top:9px;display:flex;align-items:center;gap:7px}
.brand-mark{width:26px;height:26px;border-radius:50%;background:#d52b2b}
.brand-name{font-weight:700;font-size:20px;color:var(--white);letter-spacing:.2px}
.brand-tag{left:77px;top:31px;font-size:8px;letter-spacing:2.6px;color:var(--white)}
.lights-strip{left:0;top:42px;width:675px;height:34px;background:linear-gradient(#161616,#050505)}
.lamp{top:60px;width:30px;height:10px;border-radius:50%;background:radial-gradient(#fffbe0 30%,#c7b96a 60%,transparent 75%)}
.light-band{left:0;top:76px;width:675px;height:42px;background:linear-gradient(#f2f8f8,var(--light-band))}

/* navigation */
.main-nav{left:46px;top:129px;width:591px;height:28px;border:1px solid #555;background:linear-gradient(#3b3b3b,#0d0d0d);display:flex;align-items:center;justify-content:space-around;padding:0 18px}
.main-nav a{color:var(--white);text-decoration:none;font-size:12.5px}

.page-title{left:0;top:186px;width:675px;text-align:center;font-size:38px;letter-spacing:.5px;color:transparent;background:linear-gradient(#ffffff,#8b8b8b 60%,#4a4a4a);-webkit-background-clip:text;background-clip:text}
.title-glow{left:0;top:170px;width:675px;height:80px;background:radial-gradient(ellipse at center,#2b2b2b,transparent 70%)}

/* hero */
.hero{left:44px;top:263px;width:594px;height:309px;border:2px solid #555;border-radius:8px;background:radial-gradient(ellipse at 55% 45%,#5ea83a,#2f6a1f 70%,#1f4a14)}
.hero-arrow{top:395px;width:24px;height:44px;background:#222;border:1px solid #555}
.hero-arrow.prev{left:28px;border-radius:22px 0 0 22px}
.hero-arrow.next{left:630px;border-radius:0 22px 22px 0}

/* white stage */
.stage{left:36px;top:577px;width:601px;height:424px}

.info-box{top:618px;width:145px;height:165px;background:var(--white);border:1px solid var(--box-border);border-radius:3px}
.info-box h3{font-size:8.5px;color:var(--green);font-weight:700;line-height:11px;height:40px;padding:14px 13px 0;border-bottom:1px solid var(--box-border)}
.info-box p,.info-box li{font-size:8.5px;color:var(--body-text);line-height:11px}
.info-box p{padding:16px 14px 0}
.info-box ol{padding:16px 14px 0 14px;list-style:none}
.info-box li{margin-bottom:10px}
.read-more{position:absolute;left:15px;bottom:22px;font-size:8px;color:#3a5aa8;padding:3px 7px;border:1px solid #aab;border-radius:8px;background:linear-gradient(#fff,#e4e6ee)}
.box-shooting{left:76px}
.box-moon{left:266px}
.box-check{left:460px}
.moon-title{display:flex;align-items:center;gap:8px;padding:8px 10px 0!important}
.moon-icon{width:22px;height:22px;border-radius:50%;background:radial-gradient(#cfcfcf,#666)}
.moon-form{font-family:"Caladea",Georgia,serif;font-size:8.5px;color:#555}
.field{position:absolute;height:11px;background:var(--field);border:1px solid #333;color:#fff;font-size:6px;line-height:9px;padding-left:2px}
.btn-orange{position:absolute;background:var(--orange);color:#fff;font-size:7px;text-align:center;line-height:11px}
.drop{position:absolute;width:12px;height:11px;background:#111}
.drop::after{content:"";position:absolute;left:3px;top:3px;border-left:3px solid transparent;border-right:3px solid transparent;border-top:5px solid var(--green-bright)}

/* photo slider */
.photo-slider{left:74px;top:814px;width:531px;height:137px;background:#070707;border:2px solid #777;border-radius:3px}
.slider-title{left:100px;top:826px;font-size:11.5px;color:var(--green-bright);text-decoration:underline}
.thumb{top:849px;height:59px}
.thumb-label{top:920px;font-size:9.5px;color:var(--green-bright);text-align:center}
.slider-arrow{top:877px;width:22px;height:13px;background:linear-gradient(#999,#333)}

/* footer */
.footer-info{left:0;top:1020px;width:675px;height:111px;background:var(--footer-grey);font-family:"Caladea",Georgia,serif}
.footer-heading{font-size:9.5px;color:var(--text-muted)}
.footer-text{font-size:8.5px;line-height:16.5px;color:var(--white)}
.footer-text .more{color:var(--orange)}
.gallery-thumb{width:44px;height:26px;border:2px solid #eee;border-radius:3px}
.map-area{left:310px;top:1057px;width:98px;height:47px;background:linear-gradient(135deg,#dfe6df,#b9c8d8)}
.footer-bottom{left:0;top:1131px;width:675px;height:69px;background:var(--black)}
.legal{left:47px;top:1168px;font-size:6.5px;line-height:10px;color:var(--white)}
.legal .accent{color:var(--orange)}
.find-us{left:274px;top:1164px;font-size:12px;font-weight:700;color:#3d4fa0}
.social-circle{left:344px;top:1152px;width:36px;height:36px;border-radius:50%;background:linear-gradient(#6aa6e8,#24589e);border:3px solid #ccc}
.partner{font-weight:700;font-size:15px;color:#8a8a8a}
</style>
</head>
<body>

<header>
  <div class="abs top-bar"></div>
  <div class="abs brand"><span class="brand-mark"></span><span class="brand-name">Your Frame Friend</span></div>
  <div class="abs brand-tag">PHOTOGRAPHIC TUITION</div>
  <div class="abs lights-strip"></div>
  <span class="abs lamp" style="left:38px"></span>
  <span class="abs lamp" style="left:180px"></span>
  <span class="abs lamp" style="left:323px"></span>
  <span class="abs lamp" style="left:470px"></span>
  <span class="abs lamp" style="left:610px"></span>
  <div class="abs light-band"></div>
  <nav class="abs main-nav">
    <a href="#">Home</a><a href="#">About us</a><a href="#">Our Courses</a><a href="#">Members Area</a><a href="#">Contact Us</a>
  </nav>
</header>

<div class="abs title-glow"></div>
<h1 class="abs page-title">PHOTOGRAPHIC</h1>

<section>
  <div class="abs hero" role="img" aria-label="Banner: photographer with camera beside a red macaw on a green background"></div>
  <div class="abs hero-arrow prev"><svg width="24" height="44"><path d="M17 10 L7 22 L17 34" stroke="#c31414" stroke-width="4" fill="none"/></svg></div>
  <div class="abs hero-arrow next"><svg width="24" height="44"><path d="M7 10 L17 22 L7 34" stroke="#c31414" stroke-width="4" fill="none"/></svg></div>
</section>

<svg class="abs stage" viewBox="0 0 601 424">
  <defs>
    <linearGradient id="stageFill" x1="0" y1="0" x2="0" y2="1">
      <stop offset="0" stop-color="#ffffff"/><stop offset=".85" stop-color="#f6f6f6"/><stop offset="1" stop-color="#cfcfcf"/>
    </linearGradient>
  </defs>
  <path d="M14 0 H587 Q601 0 601 14 V380 Q601 405 560 410 Q300 435 40 410 Q0 405 0 395 Q12 380 12 360 V14 Q12 0 14 0Z" fill="url(#stageFill)"/>
</svg>

<section>
  <article class="abs info-box box-shooting">
    <h3>Daily Shooting Times<br>Nautical twilight star to end</h3>
    <p>Lorem ipsum dolor sit amet, consectetur adipiscing elit. Aliquam tincidunt mi id libero egestas ut interdum nibh cursus.</p>
    <a class="read-more" href="#">Read More &gt;</a>
  </article>

  <article class="abs info-box box-moon">
    <h3 class="moon-title"><span class="moon-icon" role="img" aria-label="Moon"></span>Moon Phase Chart</h3>
    <div class="moon-form">
      <span class="abs" style="left:4px;top:57px">Date</span>
      <span class="field" style="left:25px;top:55px;width:40px">03/04/2005</span>
      <span class="abs" style="left:68px;top:57px">Time</span>
      <span class="field" style="left:92px;top:55px;width:36px">4:32 AM</span>
      <span class="btn-orange" style="left:132px;top:55px;width:20px">New</span>
      <span class="abs" style="left:4px;top:79px">Time Zone :</span>
      <span class="field" style="left:76px;top:76px;width:64px">-7:00 (MST)</span><span class="drop" style="left:139px;top:76px"></span>
      <span class="abs" style="left:4px;top:101px">Latitude :</span>
      <span class="field" style="left:68px;top:98px;width:17px">40</span><span class="field" style="left:86px;top:98px;width:17px">32</span><span class="field" style="left:104px;top:98px;width:17px">0</span><span class="field" style="left:122px;top:98px;width:14px">N</span><span class="drop" style="left:139px;top:98px"></span>
      <span class="abs" style="left:4px;top:123px">Longitude :</span>
      <span class="field" style="left:68px;top:120px;width:17px">112</span><span class="field" style="left:86px;top:120px;width:17px">18</span><span class="field" style="left:104px;top:120px;width:17px">0</span><span class="field" style="left:122px;top:120px;width:14px">W</span><span class="drop" style="left:139px;top:120px"></span>
      <span class="btn-orange" style="left:118px;top:141px;width:34px;height:12px">Apply</span>
    </div>
  </article>

  <article class="abs info-box box-check">
    <h3 style="padding-top:14px">Photographer Check List</h3>
    <ol>
      <li>1. Weddin Shoot List.</li>
      <li>2. Pre shoot checklist.</li>
      <li>3. Standard checklist.</li>
    </ol>
    <a class="read-more" href="#">Read More &gt;</a>
  </article>
</section>

<section>
  <div class="abs photo-slider"></div>
  <div class="abs slider-title">Photo Slider</div>
  <span class="abs slider-arrow" style="left:67px"></span>
  <span class="abs slider-arrow" style="left:586px"></span>
  <div class="abs thumb" role="img" aria-label="Pier at sunset" style="left:100px;width:73px;background:linear-gradient(#c98d8a,#6d4640)"></div>
  <div class="abs thumb" role="img" aria-label="Lake panorama" style="left:180px;width:73px;background:linear-gradient(#2f6ea6,#1a3d5a)"></div>
  <div class="abs thumb" role="img" aria-label="City skyline at night" style="left:260px;width:150px;background:linear-gradient(#1b2e5a,#3b2a18)"></div>
  <div class="abs thumb" role="img" aria-label="City tower walk" style="left:418px;width:75px;background:linear-gradient(#8fb0d0,#4b6a60)"></div>
  <div class="abs thumb" role="img" aria-label="HDR building with fountain" style="left:503px;width:75px;background:linear-gradient(#7e9bb3,#8a6a3b)"></div>
  <span class="abs thumb-label" style="left:96px;width:80px">Urdan Excursion</span>
  <span class="abs thumb-label" style="left:178px;width:76px">Panorma</span>
  <span class="abs thumb-label" style="left:260px;width:150px">Night Photography &amp; Night vision</span>
  <span class="abs thumb-label" style="left:416px;width:78px">City Walks</span>
  <span class="abs thumb-label" style="left:502px;width:76px">HDR</span>
</section>

<footer>
  <div class="abs footer-info"></div>
  <div class="abs footer-heading" style="left:47px;top:1039px;font-family:'Caladea',serif">Testimonials</div>
  <p class="abs footer-text" style="left:47px;top:1056px;width:175px;font-family:'Caladea',serif">Your Frame Friend photographic workshop have provided excellent training and I can show off my pictures to my friends and family members. <span class="more">Read More...</span></p>
  <div class="abs footer-heading" style="left:248px;top:1039px;font-family:'Caladea',serif">Map</div>
  <p class="abs footer-text" style="left:248px;top:1054px;width:165px;font-family:'Caladea',serif;text-align:justify">Photography<br>Blog General<br>Information &amp;<br>YFF's 2012 USA Fall Tour Travel Blog</p>
  <div class="abs map-area" role="img" aria-label="Map of tour locations"></div>
  <div class="abs footer-heading" style="left:468px;top:1039px;font-family:'Caladea',serif">Member Gallery</div>
  <div class="abs gallery-thumb" role="img" aria-label="Sunset" style="left:468px;top:1056px;background:linear-gradient(#f0a030,#402010)"></div>
  <div class="abs gallery-thumb" role="img" aria-label="City at night" style="left:531px;top:1056px;background:linear-gradient(#2a3a6a,#101830)"></div>
  <div class="abs gallery-thumb" role="img" aria-label="Mountain lake" style="left:593px;top:1056px;background:linear-gradient(#6fa0d0,#3a5a40)"></div>
  <div class="abs gallery-thumb" role="img" aria-label="Pink sky" style="left:468px;top:1092px;background:linear-gradient(#e07aa0,#604050)"></div>
  <div class="abs gallery-thumb" role="img" aria-label="Coastline" style="left:531px;top:1092px;background:linear-gradient(#7aa8d8,#c08040)"></div>
  <div class="abs gallery-thumb" role="img" aria-label="Orange canyon" style="left:593px;top:1092px;background:linear-gradient(#e08020,#5a2008)"></div>

  <div class="abs footer-bottom"></div>
  <p class="abs legal">Copyright © 2012 <span class="accent">Your Frame Friend .</span><br>Privacy Policy | Terms &amp; Conditions</p>
  <span class="abs find-us">Find Us On</span>
  <span class="abs social-circle"></span>
  <span class="abs partner" style="left:470px;top:1142px">Lumora</span>
  <span class="abs partner" style="left:576px;top:1140px">Kestrel</span>
  <span class="abs partner" style="left:470px;top:1168px">Veltro</span>
  <span class="abs partner" style="left:572px;top:1168px">Halvard</span>
</footer>

</body>
</html>
```